Delegate Welcome sign

The Copperfield Lodge hotel in Pine Bush NY is welcoming delegations from many different countries during 2019. We want to make a welcome sign about 16:9 ratio about 4 feet high with raised letters. I have attached a background design that we liked and a template with the wording. As you will see I need help with it.

```html
<!DOCTYPE html>
<html lang="en">
<head>
<meta charset="utf-8">
<title>The Copperfield Lodge Hotel – Delegate Welcome Sign</title>
<link rel="stylesheet" href="https://fonts.googleapis.com/css2?family=Montserrat:wght@600;700&family=Yellowtail&display=swap">
<style>
  :root {
    --crimson: #c0113f;
    --red: #e2283c;
    --orange: #f0621f;
    --amber: #f6a41c;
    --yellow: #fbe35c;
    --ink: #ffffff;
  }
  html, body {
    margin: 0;
    padding: 0;
    width: 1200px;
    height: 544px;
    overflow: hidden;
    background: #ffffff;
  }
  .welcome-sign {
    position: relative;
    width: 1200px;
    height: 544px;
    overflow: hidden;
    color: var(--ink);
    font-family: "Montserrat", Arial, sans-serif;
    text-align: center;
  }
  .sign-backdrop {
    position: absolute;
    inset: 0;
    background:
      radial-gradient(ellipse at 8% 0%, rgba(150, 0, 45, 0.55) 0%, rgba(150, 0, 45, 0) 45%),
      linear-gradient(118deg, var(--crimson) 0%, var(--red) 28%, var(--orange) 55%, var(--amber) 78%, var(--yellow) 100%);
  }
  .sign-line {
    position: absolute;
    left: 0;
    right: 0;
    margin: 0;
    line-height: 1;
  }
  .hotel-name {
    top: 36px;
    font-size: 33px;
    font-weight: 600;
    letter-spacing: 1.5px;
  }
  .welcome-word {
    top: 70px;
    font-family: "Yellowtail", cursive;
    font-weight: 400;
    font-size: 200px;
    line-height: 1.05;
    letter-spacing: 2px;
  }
  .delegates,
  .destination {
    font-size: 40px;
    font-weight: 600;
    letter-spacing: 1.5px;
  }
  .delegates { top: 363px; }
  .destination { top: 427px; }
  .hashtag {
    top: 497px;
    font-size: 27px;
    font-weight: 600;
    letter-spacing: 1px;
  }
</style>
</head>
<body>
  <main class="welcome-sign">
    <div class="sign-backdrop" role="img" aria-label="Faceted low-poly triangle pattern shading from crimson through orange to yellow"></div>
    <p class="sign-line hotel-name">THE COPPERFIELD LODGE HOTEL</p>
    <h1 class="sign-line welcome-word">Welcome</h1>
    <p class="sign-line delegates">2019 INTERNATIONAL DELEGATES</p>
    <p class="sign-line destination">TO THE HUDSON VALLEY IN NEW YORK</p>
    <p class="sign-line hashtag">#COPPERFIELDLODGEHOTEL</p>
  </main>
</body>
</html>
```